Swing Dance Themed Cleaning Company Website

We need a website designed for a cleaning company based in Portland, Oregon called Foxtrot Lane. We clean homes and commercial buildings, inside and out.

needs to be vintage and like the velvet moonbeam. Speakeasy 1920s feel.
needs to be classy.

Check out foxtrotlane.com We are not happy with the site currently.

please look at house scout site for more content https://www.housescoutly.com/rated.FoxtrotLaneCleaning.41827463.html

Check out my videos on my ClipTube channel Foxtrot Lane

Target Market(s)

middle class and home owner

Industry/Entity Type

Cleaning Service

Number of Pages Required

3 page

Font styles to use
Other font styles liked:
• jazzrag

Colors

Designer to choose colors to be used in the design.

Requirements
Must have
• must be good on pc and mobile

```html
<!DOCTYPE html>
<html lang="en">
<head>
<meta charset="utf-8">
<title>Foxtrot Lane — Portland Cleaning Services</title>
<link href="https://fonts.googleapis.com/css2?family=Montserrat:wght@400;600;700;800&family=Open+Sans:wght@400;600;700&family=Poiret+One&display=swap" rel="stylesheet">
<style>
:root{
  --yellow:#f5e000;
  --ink:#141414;
  --dark:#1f1f1f;
  --grey:#6b6b6b;
  --light:#f4f4f4;
  --white:#ffffff;
}
*{box-sizing:border-box;margin:0;padding:0}
html,body{width:1200px;height:3620px;overflow:hidden}
body{font-family:"Open Sans",Arial,sans-serif;color:var(--ink);background:var(--white);position:relative}
.section{position:absolute;left:0;width:1200px}
.heading{font-family:"Poiret One","Josefin Sans",sans-serif;font-size:40px;letter-spacing:2px;text-transform:uppercase;text-align:center;font-weight:400}
.btn{display:inline-block;font-family:"Montserrat",sans-serif;font-weight:700;font-size:17px;padding:14px 30px;border-radius:3px;background:var(--yellow);color:var(--ink);text-decoration:none}
.btn-outline{background:var(--white);border:2px solid var(--ink)}

/* hero */
.hero{top:0;height:620px;clip-path:polygon(0 0,100% 0,100% 560px,50% 620px,0 560px)}
.hero-bg{position:absolute;inset:0;background:linear-gradient(180deg,#3a3433 0%,#27201f 45%,#4a3f3a 100%)}
.hero-bg::after{content:"";position:absolute;inset:0;background:rgba(0,0,0,.45)}
.nav{position:absolute;top:0;left:0;width:100%;height:86px;display:flex;align-items:center;padding:0 70px;z-index:2}
.brand{display:flex;flex-direction:column}
.brand-row{display:flex;align-items:center;gap:10px}
.brand-dot{width:14px;height:14px;border-radius:50%;background:var(--yellow)}
.brand-name{font-family:"Montserrat",sans-serif;font-weight:600;font-size:24px;line-height:1;color:var(--yellow)}
.brand-tag{font-family:"Montserrat",sans-serif;font-size:10px;color:var(--white);letter-spacing:.5px;margin-top:6px;margin-left:24px}
.menu{margin-left:auto;display:flex;gap:44px;align-items:center}
.menu a{font-family:"Montserrat",sans-serif;font-size:15px;color:var(--white);text-decoration:none;padding-bottom:8px}
.menu a.active{color:var(--yellow);border-bottom:3px solid var(--yellow)}
.hero-content{position:absolute;top:160px;width:100%;text-align:center;z-index:2}
.hero-title{font-family:"Montserrat",sans-serif;font-weight:600;font-size:32px;color:var(--yellow)}
.hero-sub{color:var(--white);font-size:14px;width:520px;margin:14px auto 0;line-height:1.5}
.hero-deco{font-family:"Poiret One",sans-serif;font-size:120px;color:rgba(255,255,255,.16);letter-spacing:14px;margin-top:-6px}
.play{width:74px;height:74px;border-radius:50%;background:var(--white);margin:-40px auto 0;display:flex;align-items:center;justify-content:center}
.hero .btn{margin-top:30px}

/* about */
.about{top:620px;height:380px;text-align:center}
.about .heading{margin-top:20px}
.about-lead{color:var(--grey);font-size:14px;margin-top:24px}
.about-strong{font-weight:700;font-size:20px;margin-top:8px}
.about-text{color:var(--grey);font-size:14px;width:660px;margin:12px auto 0;line-height:1.7}
.about-actions{margin-top:32px;display:flex;gap:14px;justify-content:center}

/* services */
.services{top:1000px;height:420px;background:var(--light);text-align:center;padding-top:40px}
.services-intro{color:var(--grey);font-size:14px;width:760px;margin:22px auto 0;line-height:1.7}
.service-grid{display:flex;justify-content:center;gap:70px;margin-top:40px}
.service{width:210px;text-align:left}
.service-icon{width:64px;height:64px;border-radius:50%;background:var(--ink);display:flex;align-items:center;justify-content:center;margin-left:30px}
.service h3{font-family:"Montserrat",sans-serif;font-size:17px;font-weight:700;margin-top:20px}
.service p{font-size:13px;color:var(--grey);line-height:1.6;margin-top:6px}

/* contact */
.contact{top:1400px;height:640px;clip-path:polygon(0 60px,100% 0,100% 100%,0 100%)}
.contact-bg{position:absolute;inset:0;background:linear-gradient(160deg,#2b2b2b 0%,#1c1c1c 60%,#2a2a2a 100%)}
.contact-inner{position:absolute;left:70px;top:85px;width:640px;color:var(--white)}
.contact .heading{text-align:left;font-size:34px}
.contact-intro{font-size:14px;line-height:1.6;margin-top:20px;width:420px}
.form{display:grid;grid-template-columns:1fr 1fr;gap:18px 30px;margin-top:34px}
.field{border-bottom:1px solid rgba(255,255,255,.45);padding:8px 6px;font-size:14px;color:#ddd;display:flex;justify-content:space-between}
.field.full{grid-column:1/3;height:90px}
.contact .btn{margin-top:36px;padding:14px 44px}
.dancer{position:absolute;right:70px;top:120px;width:330px;height:440px;border-radius:4px;background:linear-gradient(180deg,rgba(255,255,255,.12),rgba(255,255,255,.04))}

/* blog */
.blog{top:2040px;height:500px;text-align:center;padding-top:30px}
.cards{display:flex;justify-content:center;gap:36px;margin-top:36px}
.card{width:316px;background:var(--white);box-shadow:0 4px 18px rgba(0,0,0,.14);text-align:left;position:relative}
.card-img{height:192px;background:linear-gradient(135deg,#6d1f1f,#c2542f 50%,#2c3f5a)}
.card-img.alt{background:linear-gradient(135deg,#3e6fa8,#e9a6c2 50%,#4c8a49)}
.date{position:absolute;top:0;left:18px;width:54px;height:64px;background:var(--yellow);text-align:center;font-family:"Montserrat",sans-serif;font-weight:700;font-size:20px;padding-top:8px;line-height:1.1}
.date small{display:block;font-size:11px;font-weight:600}
.card-body{padding:24px 22px 28px}
.card h3{font-family:"Montserrat",sans-serif;font-size:15px;font-weight:700;line-height:1.4}
.card p{font-size:13px;color:var(--grey);margin-top:10px;line-height:1.5}

/* reach */
.reach{top:2560px;height:620px;clip-path:polygon(0 0,100% 40px,100% 100%,0 100%)}
.reach-bg{position:absolute;inset:0;background:linear-gradient(180deg,#2e2a26,#1b1a19 60%,#33302c)}
.reach-inner{position:absolute;top:80px;width:100%;text-align:center;color:var(--white)}
.reach .heading{font-size:34px}
.reach-text{width:720px;margin:22px auto 0;font-size:14px;line-height:1.7}
.reach-cta{color:var(--yellow);font-weight:700;font-size:15px;margin-top:28px}
.contacts{display:grid;grid-template-columns:260px 260px;gap:26px 40px;justify-content:center;margin-top:34px;text-align:left}
.contact-item{display:flex;gap:14px;align-items:center;font-size:14px}
.ci-icon{width:36px;height:36px;border-radius:50%;background:var(--yellow);display:flex;align-items:center;justify-content:center;flex:none}

/* newsletter */
.newsletter{top:3180px;height:240px;text-align:center;padding-top:40px}
.newsletter .heading{font-size:34px}
.newsletter p{color:var(--grey);font-size:13px;margin-top:10px}
.nl-form{display:flex;justify-content:center;gap:12px;margin-top:28px}
.nl-input{width:314px;height:50px;border:1px solid #999;padding:14px;text-align:left;font-size:14px;color:var(--grey)}
.nl-form .btn{height:50px}

/* footer */
.footer{top:3420px;height:200px;background:var(--yellow);text-align:center;padding-top:22px}
.footer-links{display:flex;gap:34px;justify-content:center;font-size:14px}
.footer-links a{color:var(--ink);text-decoration:none}
.rule{width:1060px;height:1px;background:rgba(0,0,0,.4);margin:24px auto 0}
.socials{display:flex;gap:12px;justify-content:center;margin-top:22px}
.socials span{width:30px;height:30px;border-radius:50%;background:var(--ink)}
.copy{font-family:"Montserrat",sans-serif;font-weight:700;font-size:13px;margin-top:30px}
</style>
</head>
<body>

<header class="section hero">
  <div class="hero-bg" role="img" aria-label="Photo of a cleaner vacuuming a dark wooden floor"></div>
  <nav class="nav">
    <div class="brand">
      <div class="brand-row"><span class="brand-dot"></span><span class="brand-name">Foxtrot Lane</span></div>
      <span class="brand-tag">Homes &amp; buildings, inside and out</span>
    </div>
    <div class="menu">
      <a class="active" href="#">Home</a>
      <a href="#">About Us</a>
      <a href="#">Our Services</a>
      <a href="#">Blog</a>
      <a href="#">Contact Us</a>
      <svg width="18" height="18" viewBox="0 0 18 18"><circle cx="7.5" cy="7.5" r="5.5" fill="none" stroke="#f5e000" stroke-width="2"/><line x1="11.5" y1="11.5" x2="16" y2="16" stroke="#f5e000" stroke-width="2.4" stroke-linecap="round"/></svg>
    </div>
  </nav>
  <div class="hero-content">
    <h1 class="hero-title">We keep your world fresh &amp; sparkling clean</h1>
    <p class="hero-sub">Classy, friendly cleaning crews for every home and business in and around Portland, Oregon.</p>
    <div class="hero-deco">PORTLAND'S</div>
    <div class="play"><svg width="26" height="28" viewBox="0 0 26 28"><polygon points="4,2 24,14 4,26" fill="#141414"/></svg></div>
    <a class="btn" href="#">Get A Quote</a>
  </div>
</header>

<section class="section about">
  <h2 class="heading">About Us</h2>
  <p class="about-lead">Making the greater Portland area clean, one building at a time</p>
  <p class="about-strong">Good people, great service</p>
  <p class="about-text">Foxtrot Lane is a family owned professional cleaning business. We provide our years of cleaning experience to homes and businesses in and around Portland, Oregon.</p>
  <div class="about-actions">
    <a class="btn" href="#">Know More</a>
    <a class="btn btn-outline" href="#">Leave A review</a>
  </div>
</section>

<section class="section services">
  <h2 class="heading">Our Services</h2>
  <p class="services-intro">We provide cleaning and janitorial services for one time and recurring needs. While this isn't an exhaustive list of available services, these are certainly the most commonly requested!</p>
  <div class="service-grid">
    <div class="service">
      <div class="service-icon"><svg width="30" height="30" viewBox="0 0 30 30"><rect x="6" y="8" width="18" height="18" rx="2" fill="#f5e000"/><rect x="11" y="3" width="8" height="6" fill="#f5e000"/></svg></div>
      <h3>Janitorial Services</h3>
      <p>Routine janitorial, Tidy cleaning, Food service sanitation, Clean room services</p>
    </div>
    <div class="service">
      <div class="service-icon"><svg width="30" height="30" viewBox="0 0 30 30"><polygon points="15,4 27,15 23,15 23,26 7,26 7,15 3,15" fill="#f5e000"/></svg></div>
      <h3>House-cleaning</h3>
      <p>Floors, Carpet cleaning, Refuse removal, Dusting, Interior windows, Blinds</p>
    </div>
    <div class="service">
      <div class="service-icon"><svg width="30" height="30" viewBox="0 0 30 30"><circle cx="15" cy="15" r="7" fill="none" stroke="#f5e000" stroke-width="4"/><rect x="13" y="2" width="4" height="6" fill="#f5e000"/><rect x="13" y="22" width="4" height="6" fill="#f5e000"/><rect x="2" y="13" width="6" height="4" fill="#f5e000"/><rect x="22" y="13" width="6" height="4" fill="#f5e000"/></svg></div>
      <h3>Maintenance</h3>
      <p>Pressure washing, Gutters, Painting, Exterior windows, Construction cleanup, Detailing</p>
    </div>
    <div class="service">
      <div class="service-icon"><svg width="30" height="30" viewBox="0 0 30 30"><polygon points="15,3 18.5,11 27,11.5 20.5,17 22.5,26 15,21 7.5,26 9.5,17 3,11.5 11.5,11" fill="#f5e000"/></svg></div>
      <h3>Event services</h3>
      <p>Event hosting at our dance studio, Event cleanup</p>
    </div>
  </div>
</section>

<section class="section contact">
  <div class="contact-bg" role="img" aria-label="Dim photo of a cleaner mopping a floor"></div>
  <div class="contact-inner">
    <h2 class="heading">Contact Us</h2>
    <p class="contact-intro">Contact us for a quote, to book a cleaning, or for any other reason. We're looking forward to hearing from you!</p>
    <div class="form">
      <div class="field">Name*</div>
      <div class="field">E-mail*</div>
      <div class="field">Phone*</div>
      <div class="field">Select <svg width="14" height="10" viewBox="0 0 14 10"><polyline points="2,2 7,7 12,2" fill="none" stroke="#f5e000" stroke-width="2"/></svg></div>
      <div class="field full">Message</div>
    </div>
    <a class="btn" href="#">Submit</a>
  </div>
  <div class="dancer" role="img" aria-label="Vintage illustration of a 1920s dancer sweeping with a broom"></div>
</section>

<section class="section blog">
  <h2 class="heading">Latest Blog</h2>
  <div class="cards">
    <article class="card">
      <div class="card-img" role="img" aria-label="Photo of a band playing at an outdoor festival stage"></div>
      <div class="date">15<small>Jul</small></div>
      <div class="card-body">
        <h3>Foxtrot Lane Returns to Riverside Rhythm Festival 2017</h3>
        <p>Foxtrot Lane returns to the Riverside Rhythm Festival this June 30 through July...</p>
      </div>
    </article>
    <article class="card">
      <div class="card-img alt" role="img" aria-label="Photo of a festival guest in a colourful sun hat"></div>
      <div class="date">16<small>May</small></div>
      <div class="card-body">
        <h3>Foxtrot Lane sponsoring Riverside Rhythm Fest 2018</h3>
        <p>Foxtrot Lane will be sponsoring the Kids Booth at the Riverside Rhythm Festival...</p>
      </div>
    </article>
    <article class="card">
      <div class="card-img" role="img" aria-label="Photo of a band playing at an outdoor festival stage"></div>
      <div class="date">15<small>Jul</small></div>
      <div class="card-body">
        <h3>Foxtrot Lane Returns to Riverside Rhythm Festival 2017</h3>
        <p>Foxtrot Lane returns to the Riverside Rhythm Festival this June 30 through July...</p>
      </div>
    </article>
  </div>
</section>

<section class="section reach">
  <div class="reach-bg" role="img" aria-label="Dark photo of a mop on a polished floor"></div>
  <div class="reach-inner">
    <h2 class="heading">Reach Out</h2>
    <p class="reach-text">We have a flexible team ready to meet your cleaning needs, servicing Multnomah, Washington, and Clackamas Counties. Offering cleaning, janitorial and maintenance services for your home, apartment or business. We provide both one time as well as weekly, bi-weekly or monthly cleaning services.</p>
    <p class="reach-cta">If you're ready to experience a professional cleaning, reach out to us now!</p>
    <div class="contacts">
      <div class="contact-item"><span class="ci-icon"><svg width="16" height="18" viewBox="0 0 16 18"><path d="M8 1a6 6 0 0 1 6 6c0 4-6 10-6 10S2 11 2 7a6 6 0 0 1 6-6z" fill="#141414"/><circle cx="8" cy="7" r="2.2" fill="#f5e000"/></svg></span>418 SE Birch St #7<br>Portland, OR 97214</div>
      <div class="contact-item"><span class="ci-icon"><svg width="16" height="16" viewBox="0 0 16 16"><path d="M3 1l3 1 1 4-2 1c1 2 2 3 4 4l1-2 4 1 1 3-2 2C7 15 1 9 1 3z" fill="#141414"/></svg></span>971-555-0148</div>
      <div class="contact-item"><span class="ci-icon"><svg width="16" height="12" viewBox="0 0 16 12"><rect x="1" y="1" width="14" height="10" fill="#141414"/><polyline points="1,1 8,7 15,1" fill="none" stroke="#f5e000" stroke-width="1.4"/></svg></span>hello@foxtrotlane.com</div>
    </div>
  </div>
</section>

<section class="section newsletter">
  <h2 class="heading">Newsletter</h2>
  <p>For latest news or updates describe our newsletter</p>
  <div class="nl-form">
    <div class="nl-input">Enter E-mail*</div>
    <a class="btn" href="#">Subscribe</a>
  </div>
</section>

<footer class="section footer">
  <div class="footer-links">
    <a href="#">Home</a><span>|</span><a href="#">About Us</a><span>|</span><a href="#">Our Services</a><span>|</span><a href="#">Blog</a><span>|</span><a href="#">Contact Us</a>
  </div>
  <div class="rule"></div>
  <div class="socials"><span></span><span></span><span></span><span></span><span></span></div>
  <p class="copy">© Foxtrot Lane - 2018, All Rights Reserved</p>
</footer>

</body>
</html>
```